Roving Falcon (hail repair) Company seeks Web design

We are looking for someone to design a website for an automotive hail damage repair business. We are a national company that travels to cities that have suffered a catastrophic hail event, where we set up for retail customers to come in and have all of their auto hail repair needs handled.
We had a website in the past, but due to a technical error it has been deleted. You can view the old webpage by going to web.archive.org and searching www.Storm-Mender.example and looking under the date June 3rd 2015. We are hoping to have something similar to the original, but more extensive and updated. We would also like to add a page that allows our customers to get an online estimate by filling in their own damage assessment. There is a great example of what we are looking for if you go to www.quickpanelfix.example and click on "Get An Estimate".

Target Market(s)

USA

Industry/Entity Type

Automotive

Number of Pages Required

5+ page

Requirements
Must have
• Mobile Friendly, easy for me to change locations on the location page along with the map. A link to google maps app from site.

```html
<!DOCTYPE html>
<html lang="en">
<head>
<meta charset="utf-8">
<title>Storm Mender – Automotive Paintless Dent Repair</title>
<link href="https://fonts.googleapis.com/css2?family=Open+Sans:wght@400;600&family=Roboto+Condensed:ital,wght@0,400;0,700;1,400;1,700&family=Roboto:wght@400;500&display=swap" rel="stylesheet">
<style>
:root{
  --gold:#d8b60a;
  --gold-dark:#b89a06;
  --page:#1c1a17;
  --storm-top:#5a4c3a;
  --storm-mid:#3a3128;
  --card:#ecebe7;
  --card-text:#555;
  --muted:#c9c6c0;
  --footer:#3a3a3a;
  --footer-bottom:#222;
  --white:#fff;
}
*{box-sizing:border-box;margin:0;padding:0}
html,body{width:945px;height:1200px;overflow:hidden}
body{
  position:relative;
  background:linear-gradient(180deg,var(--storm-top) 0,var(--storm-mid) 180px,#2a241d 420px,var(--page) 620px,var(--page) 100%);
  font-family:"Open Sans",sans-serif;color:var(--white);
}
.abs{position:absolute}
.brand{left:78px;top:36px;font-family:"Roboto Condensed",sans-serif;font-weight:700;font-size:32px;color:var(--gold);letter-spacing:.5px}
.tagline{left:305px;top:57px;font-family:"Roboto",sans-serif;font-style:italic;font-size:12px;color:var(--white)}
.search{left:683px;top:42px;width:184px;height:31px;border:1px solid #9a948a;border-radius:3px;background:rgba(30,26,22,.35);font-size:9px;color:#bbb;padding:9px 12px}
.search svg{position:absolute;right:11px;top:10px}
.slider{left:77px;top:115px;width:790px;height:401px;border:2px solid #7c7870;
  background:radial-gradient(ellipse at 40% 40%,#2b3a5c 0,#1f2b45 30%,transparent 55%),linear-gradient(90deg,#8a8d92 0,#4d5058 30%,#9a8e88 65%,#c9c3c0 100%)}
.nav{left:77px;top:115px;width:790px;height:42px}
.nav ul{position:absolute;left:0;top:0;width:100%;height:42px;list-style:none;display:flex;padding-left:53px}
.nav li{font-family:"Roboto",sans-serif;font-size:10.5px;color:var(--white);padding:0 23px;line-height:42px;border-right:1px solid rgba(0,0,0,.12)}
.nav li:last-child{border:0}
.slide-copy{left:500px;top:272px;width:300px;text-align:center;font-family:"Roboto Condensed",sans-serif;font-style:italic;font-weight:700;color:var(--gold)}
.slide-copy .name{font-size:26px;margin-bottom:6px}
.slide-copy .line{font-size:25px;line-height:29px;color:#efd84a}
.arrow{top:352px;width:28px;height:28px;border-radius:50%;background:rgba(20,20,20,.85)}
.arrow svg{position:absolute;left:8px;top:8px}
.how{left:0;top:538px;width:945px;text-align:center;font-family:"Roboto Condensed",sans-serif;font-weight:700;font-style:italic;font-size:26px}
.card{top:584px;width:258px;height:88px;background:var(--card)}
.card .icon{position:absolute;left:21px;top:19px;width:54px;height:52px;background:var(--gold);border-radius:5px}
.card .icon svg{position:absolute;left:14px;top:13px}
.card .rule{position:absolute;left:91px;top:18px;width:1px;height:52px;background:#ccc}
.card h3{position:absolute;left:105px;top:17px;font-family:"Roboto Condensed",sans-serif;font-style:italic;font-weight:400;font-size:17px;color:#555}
.card p{position:absolute;left:105px;top:47px;width:145px;font-size:8.6px;line-height:15px;color:var(--card-text)}
.sec-title{top:716px;font-family:"Roboto Condensed",sans-serif;font-weight:700;font-style:italic;font-size:21px}
.frame{top:758px;width:149px;height:154px;border:2px solid #fff}
.copy{top:756px;width:218px;font-size:8.8px;line-height:16px;color:var(--muted)}
.copy p+p{margin-top:8px}
.btn{top:886px;width:86px;height:26px;background:var(--gold);font-family:"Roboto Condensed",sans-serif;font-style:italic;font-size:11px;color:var(--white);text-align:center;line-height:26px}
.footer{left:0;top:963px;width:945px;height:196px;background:var(--footer)}
.f-title{top:1000px;font-family:"Roboto Condensed",sans-serif;font-style:italic;font-size:14.5px;line-height:18px}
.f-text{font-size:9.3px;line-height:15px;color:#eee}
.news{left:78px;top:1025px;width:150px}
.date{left:78px;top:1080px;font-size:12px;color:#eee}
.social{top:1111px;width:21px;height:21px;border-radius:50%;background:#fff}
.field{left:282px;top:1043px;width:205px;height:33px;background:#fff;font-size:8.5px;color:#666;padding:11px 10px}
.subscribe{left:282px;top:1086px;width:80px;height:33px;background:var(--gold);font-family:"Roboto",sans-serif;font-size:10.5px;text-align:center;line-height:33px}
.links{left:560px;top:1031px;list-style:none;font-size:9.5px;line-height:19px;color:#eee}
.contact{left:730px;top:1031px;font-size:10px;line-height:15.5px;color:#eee}
.contact-row{left:730px;font-size:10.5px;color:#eee;letter-spacing:.3px}
.contact-row svg{position:absolute;left:2px;top:0}
.contact-row span{position:absolute;left:29px;top:0;white-space:nowrap}
.bottom{left:0;top:1159px;width:945px;height:41px;background:var(--footer-bottom);text-align:center;font-size:9.5px;line-height:41px;color:#eee}
</style>
</head>
<body>

<header>
  <div class="abs brand">STORM MENDER</div>
  <div class="abs tagline">Automotive Paintless Dent Repair</div>
  <div class="abs search">Search Here
    <svg width="10" height="10" viewBox="0 0 10 10"><circle cx="4" cy="4" r="3" fill="none" stroke="#bbb" stroke-width="1.3"/><line x1="6.3" y1="6.3" x2="9" y2="9" stroke="#bbb" stroke-width="1.4"/></svg>
  </div>
</header>

<section class="abs slider" role="img" aria-label="Photo of a smiling mechanic in navy overalls working on an open car engine in a workshop"></section>

<nav class="abs nav">
  <svg width="790" height="42" viewBox="0 0 790 42" style="position:absolute;left:0;top:0"><polygon points="0,0 790,0 752,42 41,42" fill="var(--gold)"/></svg>
  <ul>
    <li>HOME</li><li>ABOUT US</li><li>WHAT IS PDR?</li><li>SERVICES</li><li>GALLERY</li><li>NEWS</li><li>CONTACT US</li>
  </ul>
</nav>

<div class="abs slide-copy">
  <div class="name">STORM MENDER</div>
  <div class="line">Our Work is Backed by</div>
  <div class="line">a Written Lifetime Warranty</div>
</div>
<div class="abs arrow" style="left:107px"><svg width="12" height="12" viewBox="0 0 12 12"><polyline points="8,1 3,6 8,11" fill="none" stroke="#fff" stroke-width="2"/></svg></div>
<div class="abs arrow" style="left:809px"><svg width="12" height="12" viewBox="0 0 12 12"><polyline points="4,1 9,6 4,11" fill="none" stroke="#fff" stroke-width="2"/></svg></div>

<h2 class="abs how">HOW EASY?</h2>

<div class="abs card" style="left:77px">
  <div class="icon"><svg width="26" height="26" viewBox="0 0 26 26"><rect x="2" y="6" width="22" height="15" rx="2" fill="none" stroke="#fff" stroke-width="2"/><polyline points="2,7 13,15 24,7" fill="none" stroke="#fff" stroke-width="2"/></svg></div>
  <div class="rule"></div>
  <h3>Contact Us</h3>
  <p>Lorem ipsum dolor sit amet, consectetur adipiscing elit, sed</p>
</div>
<div class="abs card" style="left:342px">
  <div class="icon"><svg width="26" height="26" viewBox="0 0 26 26"><polygon points="15,1 7,15 12,15 9,25 19,10 14,10 17,1" fill="#fff"/></svg></div>
  <div class="rule"></div>
  <h3>Drop your car off</h3>
  <p>Lorem ipsum dolor sit amet, consectetur adipiscing elit, sed</p>
</div>
<div class="abs card" style="left:609px">
  <div class="icon"><svg width="26" height="26" viewBox="0 0 26 26"><path d="M6 6h14l3 7v7h-3v3h-3v-3H9v3H6v-3H3v-7z" fill="#fff"/><rect x="7" y="8" width="12" height="5" fill="var(--gold)"/><circle cx="7" cy="16" r="1.6" fill="var(--gold)"/><circle cx="19" cy="16" r="1.6" fill="var(--gold)"/></svg></div>
  <div class="rule"></div>
  <h3>Pick your car</h3>
  <p>up Our professional staff will handle the rest!</p>
</div>

<h2 class="abs sec-title" style="left:77px">LIFETIME GUARANTEE?</h2>
<div class="abs frame" style="left:78px;background:#efeeec">
  <svg width="145" height="150" viewBox="0 0 145 150"><circle cx="72" cy="75" r="46" fill="var(--gold)"/></svg>
</div>
<div class="abs copy" style="left:242px">
  <p>That's correct, we offer a full written lifetime guarantee to all of our customers. We pride ourselves in our work and our lifetime guarantee shows it.</p>
  <p>As long as you own your vehicle if any of our work has failed we will fix the damaged area at no charge to you. Your 100% satisfaction is our top priority!</p>
</div>
<div class="abs btn" style="left:242px">LEARN MORE</div>

<h2 class="abs sec-title" style="left:490px">EASY &amp; RELIABLE SERVICE</h2>
<div class="abs frame" style="left:491px;background:linear-gradient(120deg,#e6e7ea 0,#9aa3ad 40%,#2456a8 60%,#3a3e45 100%)" role="img" aria-label="Photo of a technician in blue overalls servicing a car wheel"></div>
<div class="abs copy" style="left:655px;width:215px">
  <p>Our mission is to provide you with a stress-free experience while taking care of all of your needs in an efficient and professional manner.</p>
  <p>We want to make this process as easy for you as possible. Storm Mender is dedicated to making that a reality. We work with all major insurance carriers, and we have knowledgeable staff</p>
</div>
<div class="abs btn" style="left:655px">LEARN MORE</div>

<footer>
  <div class="abs footer"></div>
  <h4 class="abs f-title" style="left:78px">LATEST NEWS</h4>
  <p class="abs f-text news">Lorem ipsum dolor sit amet, consectetur adipiscing elit, sed do eiusmod tempor incididunt</p>
  <div class="abs date">Oct 15, 2015</div>
  <div class="abs social" style="left:77px"></div>
  <div class="abs social" style="left:100px"></div>
  <div class="abs social" style="left:123px"></div>
  <div class="abs social" style="left:146px"></div>

  <h4 class="abs f-title" style="left:282px">CONTACT US TODAY FOR<br>A FREE QUOTE!</h4>
  <div class="abs field">Enter Name</div>
  <div class="abs subscribe">SUBSCRIBE</div>

  <h4 class="abs f-title" style="left:560px">INFORMATION</h4>
  <ul class="abs links"><li>About Us</li><li>What Is Pdr?</li><li>Services</li><li>Gallery</li><li>Contact</li></ul>

  <h4 class="abs f-title" style="left:730px;top:1002px">CONTACT US</h4>
  <p class="abs contact">Storm Mender<br>4120 Elm Ridge Rd</p>
  <div class="abs contact-row" style="top:1076px">
    <svg width="14" height="14" viewBox="0 0 14 14"><path d="M3 1l2.5 3-1.5 1.5c1 2 2.5 3.5 4.5 4.5L10 8.5l3 2.5-1.5 2C7 13 1 7 1 2.5z" fill="none" stroke="#ddd" stroke-width="1"/></svg>
    <span>+1 555 0142 7730</span>
  </div>
  <div class="abs contact-row" style="top:1096px">
    <svg width="15" height="12" viewBox="0 0 15 12"><rect x="1" y="1.5" width="13" height="9" fill="none" stroke="#ddd" stroke-width="1"/><polyline points="1,2 7.5,7 14,2" fill="none" stroke="#ddd" stroke-width="1"/></svg>
    <span>info@storm-mender.example</span>
  </div>

  <div class="abs bottom">Copyright©2016 Storm Mender.All Rights Reserved</div>
</footer>

</body>
</html>
```